banner for website

I need a new banner for my website. My website now is. www.brightmeadowkitchen.net, but I'm changing it to Fresh Rooted Days and I need a new banner. I want me to be who it's about. I am my brand. I'm Marla Prewitt. So, my name needs to be prominent in the banner along with my photo, which I'm attaching. I want my photo very prominent in the banner and very large. I am attaching my two favorites.
I need the banner plain ( with out the newsletter sign up optin part), so I can use it on my newsletters, emails and letter head, as well. I would like it to be inviting. I I have a certain color scheme I use. Deep dark brown letters with blues and greens. Very earthy and psychologically grounded. I would like to keep that color scheme. In my website banner, I need a opt in to sign up for my free monthly newsletter and receive my Free Pantry Starter Booklet.

I want the shopping guide to be small and pleasant looking and to say: "Sign up to receive your Free Pantry Starter Booklet and monthly newsletter."

I only want my banner to say: "Fresh Rooted Days" "Marla Prewitt"

I would also like to have part of the banner without the sign in for the newsletter part off of it. And also one with only the "Fresh Rooted Days" and one with "Fresh Rooted Days" and "Marla Prewitt" without the newsletter sign up part on it either.

I hope you can do this for me. I look forward to seeing your design! Sincerely, Marla
Updates

Project Deadline Extended Reason: I couldn't view the designs so I couldn't look at the ones submitted. I just now got into the website with your company's help. I don't want to be penalized because of a problem with the log in at your site. That was not my fault. Please let me know your thoughts. Added Monday, May 9, 2016

Target Market(s)

people over 40 who have bad health or who want to learn how to be a vegetarian for better health.

Number of Pages Required

1 page

Requirements
Must have
• I want the shopping guide to be small and pleasant looking and to say: "Sign up to receive your Free Pantry Starter Booklet and monthly newsletter." I would like it to blend and be elegant and not in the middle of the banner or across my face.
• I only want my banner to say: "Fresh Rooted Days" "Marla Prewitt"
• I would also like to have part of the banner without the sign in for the newsletter part off of it. And also one with only the "Fresh Rooted Days" and one with "Fresh Rooted Days" and "Marla Prewitt" without the newsletter sign up part on it either.
Nice to have
• Nice font and colors. I want the background to be plants and earthy and inviting.
Should not have
• I updated and added two new photos. I think the one you were using with me in the red top looked funny under my eyes. it was too pink or something. I uploaded a better version of that photo. in hopes that it looks better. Please switch those out if you are using the one with me in the red top.

```html
<!DOCTYPE html>
<html lang="en">
<head>
<meta charset="utf-8">
<title>Fresh Rooted Days – Marla Prewitt</title>
<link rel="stylesheet" href="https://fonts.googleapis.com/css2?family=Great+Vibes&family=Courgette&display=swap">
<style>
  :root {
    --bg-left: #3d7d5c;
    --bg-mid: #1e4f4c;
    --bg-right: #2c5f4b;
    --text-brown: #3a2314;
    --text-halo: #f3eedc;
    --vine-green: #8fb07a;
    --vine-pale: #dfe8cf;
    --portrait-light: #e9c9a8;
    --portrait-warm: #b24a3c;
    --portrait-hair: #e6cf9a;
  }
  html, body {
    margin: 0;
    padding: 0;
    width: 1200px;
    height: 308px;
    overflow: hidden;
    background: #ffffff;
  }
  .banner {
    position: relative;
    width: 1200px;
    height: 308px;
    overflow: hidden;
    background: linear-gradient(90deg, var(--bg-left) 0%, var(--bg-mid) 55%, var(--bg-right) 100%);
  }
  .portrait {
    position: absolute;
    left: 0;
    top: 0;
    width: 235px;
    height: 308px;
    background:
      radial-gradient(ellipse 70px 90px at 110px 95px, var(--portrait-light) 0%, rgba(233,201,168,0) 100%),
      radial-gradient(ellipse 120px 110px at 95px 90px, var(--portrait-hair) 0%, rgba(230,207,154,0) 100%),
      linear-gradient(180deg, rgba(178,74,60,0) 45%, var(--portrait-warm) 75%, #6f8a4e 100%),
      linear-gradient(90deg, #5f8a63 0%, #4a7a5c 100%);
  }
  .ornament {
    position: absolute;
    border-radius: 60px;
    opacity: 0.75;
  }
  .ornament--top-left {
    left: 180px; top: -40px; width: 470px; height: 80px;
    background: linear-gradient(90deg, var(--vine-green), var(--vine-pale), rgba(143,176,122,0));
  }
  .ornament--bottom {
    left: 220px; top: 262px; width: 980px; height: 90px;
    background: linear-gradient(90deg, rgba(143,176,122,0), var(--vine-green) 20%, var(--vine-pale) 55%, var(--vine-green) 85%, rgba(143,176,122,0.4));
  }
  .ornament--top-right {
    left: 980px; top: -45px; width: 240px; height: 60px;
    background: linear-gradient(90deg, rgba(143,176,122,0), var(--vine-pale) 40%, var(--vine-green));
  }
  .ornament--right-side {
    left: 1175px; top: 175px; width: 60px; height: 110px;
    background: linear-gradient(180deg, var(--vine-green), var(--vine-pale), var(--vine-green));
  }
  .brand {
    position: absolute;
    left: 205px;
    top: 62px;
    width: 690px;
    margin: 0;
    text-align: center;
    font-family: "Great Vibes", cursive;
    font-weight: 400;
    color: var(--text-brown);
    text-shadow: 0 0 3px var(--text-halo), 0 0 8px var(--text-halo), 0 0 14px var(--text-halo);
  }
  .brand__title {
    display: block;
    font-size: 84px;
    line-height: 1;
  }
  .brand__name {
    display: block;
    font-size: 80px;
    line-height: 1;
    margin-top: 12px;
  }
  .optin {
    position: absolute;
    left: 805px;
    top: 28px;
    width: 380px;
    margin: 0;
    text-align: center;
    font-family: "Courgette", cursive;
    font-size: 27px;
    line-height: 1.25;
    color: var(--text-brown);
    text-shadow: 0 0 3px var(--text-halo), 0 0 7px var(--text-halo), 0 0 12px var(--text-halo);
  }
</style>
</head>
<body>
  <div class="banner">
    <div class="portrait" role="img" aria-label="Portrait photo of Marla Prewitt holding a basket of fresh vegetables"></div>
    <div class="ornament ornament--top-left" role="img" aria-label="Decorative vine with white roses along the top edge"></div>
    <div class="ornament ornament--bottom" role="img" aria-label="Decorative vine with leaves and white roses along the bottom edge"></div>
    <div class="ornament ornament--top-right" role="img" aria-label="Decorative white rose cluster in the top right corner"></div>
    <div class="ornament ornament--right-side" role="img" aria-label="Decorative leaves along the right edge"></div>

    <h1 class="brand">
      <span class="brand__title">Fresh Rooted Days</span>
      <span class="brand__name">Marla Prewitt</span>
    </h1>

    <p class="optin">
      Sign up to receive your<br>
      Free Pantry Starter<br>
      Booklet and monthly<br>
      newsletter.
    </p>
  </div>
</body>
</html>
```